Computer tuition business needs Business card and Advertising Flyer

I am starting up a new business "Dorian Featherby Computer Services" (DFCS for short) based in the Manning Valley NSW Australia.
The primary focus is on tuition\advice to the elderly and less computer literate in the region.
I will not be providing any repair services.

I have the line "At your home, On your computer, Answering your questions" in my head

I will need a Business card design (one sided) and Advertising Flyer design (A4 size, grayscale ).

Contact details on all these are - Mobile: 0412-683-904
- Email : dfeatherby.techhelp@examplemail.net

Target Market(s)

The primary focus is on tuition\advice to the elderly and less computer literate in the Manning Valley region of

Industry/Entity Type

Computer

```html
<!DOCTYPE html>
<html lang="en">
<head>
<meta charset="utf-8">
<title>DFCS Flyer</title>
<link rel="stylesheet" href="https://fonts.googleapis.com/css2?family=Bebas+Neue&family=Roboto+Condensed:wght@300;400&family=Roboto:wght@700;900&display=swap">
<style>
  :root {
    --page-bg: #d9d9d9;
    --ink: #111111;
    --white: #ffffff;
    --band-dark: #3a3a3a;
    --band-mid: #6e6e6e;
    --band-light: #cfcfcf;
    --screen-text: #666666;
    --call-box: #2b2b2b;
    --call-text: #b5b5b5;
  }
  * { margin: 0; padding: 0; box-sizing: border-box; }
  html, body {
    width: 900px;
    height: 1200px;
    overflow: hidden;
    background: var(--page-bg);
  }
  .canvas {
    position: relative;
    width: 900px;
    height: 1200px;
  }
  .flyer {
    position: absolute;
    left: 30px;
    top: 29px;
    width: 840px;
    height: 1142px;
    box-shadow: 0 4px 18px rgba(0,0,0,0.25);
  }
  .flyer svg { display: block; width: 100%; height: 100%; }
  .headline { font-family: "Bebas Neue", sans-serif; fill: var(--ink); }
  .brand-name { font-family: "Roboto", sans-serif; font-weight: 900; }
  .focus-text { font-family: "Roboto Condensed", sans-serif; font-weight: 300; fill: var(--white); }
  .call-text { font-family: "Bebas Neue", sans-serif; }
  .email { font-family: "Roboto", sans-serif; font-weight: 700; fill: var(--ink); }
</style>
</head>
<body>
<main class="canvas">
  <article class="flyer">
    <svg viewBox="0 0 710 965" xmlns="http://www.w3.org/2000/svg">
      <defs>
        <linearGradient id="top-band" x1="0" y1="0" x2="1" y2="1">
          <stop offset="0" stop-color="#9a9a9a"/>
          <stop offset="0.5" stop-color="#d8d8d8"/>
          <stop offset="1" stop-color="#b4b4b4"/>
        </linearGradient>
        <linearGradient id="dark-band" x1="0" y1="0" x2="1" y2="0">
          <stop offset="0" stop-color="#2f2f2f"/>
          <stop offset="0.6" stop-color="#555555"/>
          <stop offset="1" stop-color="#3a3a3a"/>
        </linearGradient>
        <linearGradient id="light-strip" x1="0" y1="0" x2="1" y2="0">
          <stop offset="0" stop-color="#a8a8a8"/>
          <stop offset="1" stop-color="#ececec"/>
        </linearGradient>
        <linearGradient id="photo-tone" x1="0" y1="0" x2="0" y2="1">
          <stop offset="0" stop-color="#5a5a5a"/>
          <stop offset="1" stop-color="#2e2e2e"/>
        </linearGradient>
        <linearGradient id="call-box" x1="0" y1="0" x2="0" y2="1">
          <stop offset="0" stop-color="#1f1f1f"/>
          <stop offset="1" stop-color="#4a4a4a"/>
        </linearGradient>
      </defs>

      <!-- base -->
      <rect class="flyer-base" width="710" height="965" fill="url(#dark-band)"/>

      <!-- top band -->
      <path class="top-band" d="M0 0 H710 V170 C560 220 330 240 0 310 Z" fill="url(#top-band)"/>
      <path class="top-band-shade" d="M0 0 H710 V70 C520 20 250 50 0 110 Z" fill="#5a5a5a" opacity="0.55"/>
      <path class="top-swoosh" d="M0 110 C250 50 520 20 710 70" fill="none" stroke="var(--white)" stroke-width="3"/>
      <rect class="top-photo" role="img" aria-label="Faint photo of a bank card and a globe" x="205" y="8" width="345" height="120" rx="14" fill="#ffffff" opacity="0.12" transform="rotate(-6 377 68)"/>

      <!-- mid dark ribbon -->
      <path class="mid-ribbon" d="M0 310 C330 240 560 220 710 170 V200 C560 250 300 270 0 345 Z" fill="#4a4a4a"/>
      <path d="M0 312 C330 242 560 222 710 172" fill="none" stroke="var(--white)" stroke-width="3"/>

      <!-- central white field -->
      <path class="white-field" d="M0 345 C300 270 560 250 710 200 V590 C520 640 260 660 0 665 Z" fill="var(--white)"/>
      <path d="M40 640 C200 660 420 630 640 575" fill="none" stroke="#dddddd" stroke-width="10"/>

      <!-- lower light strip -->
      <path class="light-strip" d="M0 885 C250 890 520 860 710 815 V965 H0 Z" fill="url(#light-strip)"/>
      <path d="M0 885 C250 890 520 860 710 815" fill="none" stroke="var(--white)" stroke-width="3"/>

      <!-- logo -->
      <text class="brand-name" x="112" y="128" text-anchor="middle" font-size="40" fill="var(--white)">DFCS</text>

      <!-- headline -->
      <text class="headline" x="218" y="86" font-size="37" letter-spacing="0.5">AT YOUR HOME, ON YOUR COMPUTER,</text>
      <text class="headline" x="218" y="143" font-size="46" letter-spacing="0.5">ANSWERING YOUR QUESTIONS</text>

      <!-- hero photo -->
      <rect class="hero-photo" role="img" aria-label="Photo of a large open laptop with a seated businesswoman and a standing businessman beside it" x="140" y="272" width="462" height="390" rx="6" fill="url(#photo-tone)"/>
      <rect class="hero-screen" x="185" y="295" width="335" height="243" fill="var(--white)"/>
      <text class="brand-name" x="352" y="445" text-anchor="middle" font-size="96" fill="var(--screen-text)">DFCS</text>

      <!-- focus statement -->
      <text class="focus-text" x="48" y="760" font-size="30">THE PRIMARY FOCUS IS</text>
      <text class="focus-text" x="48" y="800" font-size="30">ON TUITION\ADVICE TO</text>
      <text class="focus-text" x="48" y="832" font-size="19.5">THE ELDERLY AND LESS COMPUTER</text>
      <text class="focus-text" x="48" y="870" font-size="29">LITERATE IN THE REGION</text>

      <!-- call box -->
      <rect class="call-box" x="435" y="713" width="205" height="135" rx="18" fill="url(#call-box)"/>
      <text class="call-text" x="537" y="780" text-anchor="middle" font-size="42" fill="var(--call-text)">CALL TODAY</text>
      <text class="call-text" x="537" y="818" text-anchor="middle" font-size="33" fill="var(--white)">0412-683-904</text>

      <!-- email -->
      <text class="email" x="665" y="936" text-anchor="end" font-size="17">dfeatherby.techhelp@examplemail.net</text>
    </svg>
  </article>
</main>
</body>
</html>
```